Business Card Design

I need a business card design for a new company based in Sydney called 'The Brisk Ladle'. We deliver organic, gourmet and fine foods to your door.

I would like to see creative, unique designs which use colours which represent health and nature like green.

Target Market(s)

Health conscious 20 to 35 year olds.

Industry/Entity Type

Health

Contact Information for Business Card

The Brisk Ladle, Owen Pardalis, owen@thebriskladle.com.au, 0427865193

Requirements
Must have
• My logo.

```html
<!DOCTYPE html>
<html lang="en">
<head>
<meta charset="utf-8">
<title>The Brisk Ladle — Business Card</title>
<link rel="stylesheet" href="https://fonts.googleapis.com/css2?family=Comfortaa:wght@400&family=Oswald:wght@600&family=Poppins:wght@300&display=swap">
<style>
  :root {
    --canvas: #e7e5e1;
    --card: #f4f3ef;
    --green-bright: #8cc63f;
    --green-mid: #6aa632;
    --green-dark: #2f5e1e;
    --ink: #2b2b2b;
    --dots: #3a3a3a;
  }
  * { margin: 0; padding: 0; box-sizing: border-box; }
  html, body {
    width: 1200px;
    height: 908px;
    overflow: hidden;
    background: var(--canvas);
  }
  .sheet {
    width: 1200px;
    height: 908px;
    display: flex;
    flex-direction: column;
    align-items: center;
    justify-content: center;
    gap: 40px;
  }
  .card {
    position: relative;
    width: 640px;
    height: 391px;
    background: var(--card);
    box-shadow: 0 2px 10px rgba(0,0,0,0.12);
  }

  /* Back side: tagline and contact details */
  .card--back .frame {
    position: absolute;
    left: 52px;
    top: 44px;
  }
  .tagline {
    position: absolute;
    left: 78px;
    top: 62px;
    font-family: "Oswald", sans-serif;
    font-weight: 600;
    font-size: 27px;
    line-height: 34px;
    letter-spacing: 0.5px;
    color: var(--green-bright);
    text-transform: uppercase;
  }
  .contact {
    position: absolute;
    left: 150px;
    top: 168px;
    font-family: "Poppins", sans-serif;
    font-weight: 300;
    color: var(--ink);
  }
  .contact__name {
    font-size: 24px;
    margin-left: 84px;
    margin-bottom: 26px;
  }
  .contact__line {
    font-size: 17px;
    line-height: 26px;
  }
  .card--back .leaders {
    position: absolute;
    left: 110px;
    top: 172px;
  }

  /* Front side: company name */
  .card--front {
    display: flex;
    align-items: center;
    justify-content: center;
    gap: 26px;
  }
  .brand__dot {
    width: 96px;
    height: 96px;
    border-radius: 50%;
    background: var(--green-mid);
  }
  .brand__name {
    font-family: "Comfortaa", sans-serif;
    font-weight: 400;
    font-size: 62px;
    line-height: 1;
    color: var(--green-mid);
  }
</style>
</head>
<body>
<main class="sheet">

  <section class="card card--back" aria-label="Business card back">
    <svg class="frame" width="540" height="130" viewBox="0 0 540 130" aria-hidden="true">
      <polyline points="60,4 4,4 4,70" fill="none" stroke="var(--green-bright)" stroke-width="5"/>
      <polyline points="536,60 536,126 480,126" fill="none" stroke="var(--green-bright)" stroke-width="5"/>
    </svg>
    <p class="tagline">We deliver organic, gourmet<br>and fine foods to your door</p>

    <svg class="leaders" width="480" height="140" viewBox="0 0 480 140" aria-hidden="true">
      <line x1="4" y1="4" x2="4" y2="132" stroke="var(--dots)" stroke-width="3" stroke-linecap="round" stroke-dasharray="0 14"/>
      <line x1="4" y1="44" x2="80" y2="44" stroke="var(--dots)" stroke-width="3" stroke-linecap="round" stroke-dasharray="0 14"/>
      <line x1="300" y1="132" x2="470" y2="132" stroke="var(--dots)" stroke-width="3" stroke-linecap="round" stroke-dasharray="0 14"/>
    </svg>
    <div class="contact">
      <p class="contact__name">Owen Pardalis</p>
      <p class="contact__line">owen@thebriskladle.com.au</p>
      <p class="contact__line">0427865193</p>
    </div>
  </section>

  <section class="card card--front" aria-label="Business card front">
    <span class="brand__dot" aria-hidden="true"></span>
    <h1 class="brand__name">The Brisk Ladle</h1>
  </section>

</main>
</body>
</html>
```